Business card for Autism Consultancy

I need a double-sided business card for Brightpath Learning Consultancy
Please try to use the colours and graphics in line with our website www.brightpathlearn.nz
Front side
Logo and the name of the company – Brightpath Learning Consultancy
We use Child-Centred, Modern and Innovative approaches
Teaching autistic children to bond, laugh and play
www.brightpathlearn.nz
info@brightpathlearn.nz
phone +64 09 37 615 48
Back side
Photo
Mirela Dunstan
Founder
Postgraduate Autism (Children) Specialist (with Merit)
Qualified by the Faculty of Learning Support and Access Studies (FLSA), Harwell Vale University
mirela@brightpathlearn.nz
phone +64 937 615 48
mobile: +64 20 6283 9150
Please do not convert the text fields to outlines, i.e. I need to be able to edit any text after.
The final design should be either in Adobe Illustrator or Adobe Photoshop format.
The Specs for the business card are:
Full Bleed Size
94 x 58 mm
1110 x 685 pixels
Document Trim Size
91 x 55 mm
1075 x 650 pixels

```html
<!DOCTYPE html>
<html lang="en">
<head>
<meta charset="utf-8">
<title>Brightpath Learning Consultancy – Business Card</title>
<link href="https://fonts.googleapis.com/css2?family=Pathway+Gothic+One&display=swap" rel="stylesheet">
<style>
  :root {
    --backdrop: #c4c4c4;
    --card-white: #ffffff;
    --sun-yellow: #fcd423;
    --sea-teal: #52c4c0;
    --navy: #1d2b5c;
    --soft-grey: #9b9b9b;
    --ribbon-gold: #ceb04c;
  }
  html, body {
    margin: 0;
    padding: 0;
    overflow: hidden;
  }
  body {
    width: 931px;
    height: 1200px;
    background: var(--backdrop);
    position: relative;
    font-family: "Pathway Gothic One", "Arial Narrow", sans-serif;
  }
  .card {
    position: absolute;
    width: 757px;
    height: 457px;
    box-shadow: 8px 14px 22px rgba(0, 0, 0, 0.35);
    overflow: hidden;
  }
  .card svg { display: block; }
  .card--front { left: 89px; top: 63px; background: var(--card-white); }
  .card--back { left: 84px; top: 649px; background: var(--sun-yellow); }

  .brand-name { fill: var(--navy); font-size: 54px; }
  .contact-line { fill: var(--soft-grey); font-size: 28px; }
  .tagline { fill: var(--navy); font-size: 31px; }
  .person-name { fill: var(--navy); font-size: 28px; }
  .ribbon-text { fill: var(--card-white); font-size: 28px; }
  .credential { fill: var(--navy); font-size: 28px; }
  .brand-name--small { fill: var(--sea-teal); font-size: 26px; }
</style>
</head>
<body>

<section class="card card--front" aria-label="Card front">
  <svg width="757" height="457" viewBox="0 0 757 457">
    <polygon class="corner corner--top-left" points="0,0 88,0 0,88" fill="var(--sun-yellow)"/>
    <polygon class="corner corner--top-right" points="669,0 757,0 757,88" fill="var(--sun-yellow)"/>
    <polygon class="corner corner--bottom-left" points="0,369 0,457 88,457" fill="var(--sea-teal)"/>
    <polygon class="corner corner--bottom-right" points="757,369 757,457 669,457" fill="var(--sea-teal)"/>

    <circle class="brand-dot" cx="170" cy="140" r="48" fill="var(--sun-yellow)"/>
    <text class="brand-name" x="234" y="111">Brightpath Learning</text>
    <text class="brand-name" x="678" y="169" text-anchor="end">Consultancy</text>

    <text class="contact-line" x="422" y="213">www.brightpathlearn.nz</text>
    <text class="contact-line" x="422" y="257">info@brightpathlearn.nz</text>
    <text class="contact-line" x="422" y="299">phone +64 09 37 615 48</text>

    <text class="tagline" x="379" y="381" text-anchor="middle">We use Child-Centred, Modern and Innovative approaches.</text>
    <text class="tagline" x="379" y="424" text-anchor="middle">Teaching autistic children to bond, laugh and play.</text>
  </svg>
</section>

<section class="card card--back" aria-label="Card back">
  <svg width="757" height="457" viewBox="0 0 757 457">
    <defs>
      <radialGradient id="portrait-tone" cx="0.55" cy="0.55" r="0.6">
        <stop offset="0" stop-color="#d9b9a0"/>
        <stop offset="0.6" stop-color="#efe2d6"/>
        <stop offset="1" stop-color="#ffffff"/>
      </radialGradient>
    </defs>
    <polygon class="corner corner--top-left" points="0,0 88,0 0,88" fill="var(--sea-teal)"/>

    <polygon class="contact-ribbon" points="225,157 552,157 521,217 552,277 208,277" fill="var(--ribbon-gold)"/>

    <circle class="portrait" cx="81" cy="329" r="141" fill="url(#portrait-tone)" role="img" aria-label="Portrait photo of Mirela Dunstan, founder"/>

    <ellipse class="name-bubble" cx="148" cy="144" rx="97" ry="67" fill="var(--card-white)"/>
    <text class="person-name" x="148" y="138" text-anchor="middle">Mirela Dunstan</text>
    <text class="person-name" x="148" y="178" text-anchor="middle">-Founder-</text>

    <text class="ribbon-text" x="251" y="185">mirela@brightpathlearn.nz</text>
    <text class="ribbon-text" x="251" y="227">phone +64 937 615 48</text>
    <text class="ribbon-text" x="251" y="270">mobile: +64 20 6283 9150</text>

    <circle class="brand-dot" cx="630" cy="88" r="30" fill="var(--sea-teal)"/>
    <text class="brand-name--small" x="630" y="155" text-anchor="middle">Brightpath</text>
    <text class="brand-name--small" x="630" y="183" text-anchor="middle">Learning</text>

    <text class="credential" x="246" y="315">-Postgraduate Autism (Children) Specialist (with Merit)</text>
    <text class="credential" x="246" y="354">-Qualified by the Faculty of</text>
    <text class="credential" x="255" y="393">Learning Support and Access Studies (FLSA)</text>
    <text class="credential" x="246" y="431">-Harwell Vale University</text>
  </svg>
</section>

</body>
</html>
```